Fresh & Clean *NEW* BUSINESS CARD Needed - OPTOMETRY Clinic/Optical

High-tech optometry practice with 3 doctors seeking new business card.  We provide eye exams, sell, designer glasses/contacts/specialty eyewear and treat ocular diseases.  For our business cards, we are seeking fresh, clean, and crisp design as we grow our team (staffing change).  Simply adding doctors is making the card look busy/cluttered.
 Looking for professional, less cluttered look yet still have our logo, doctor names, phone, address, and website....If possible!  :)
Names:
Marcia Trelford, O.D.
Ned Pallister, O.D.
Oona Ferrant, O.D.
Phone: 555-014-2738
Website: www.BrightLensHub.example
Address:  417 Garnet R. Holloway, Larkmoor, ZZ 00000
Ultimately we have the main business card with all doctor sames and that card has two versions  (front is always the same).  The back has two designs (1) displays next appointment time/date, (2) for "general use" (non-appointment.)    I have attached what we have used in the past.  
We also need a design template for each team member in our practice with their name, title, and email.   Those should be designed with the "general use" back (see attached).
**Open to entirely new design so don't feel obligated to keep current format.  Need new perspective!  Also including our watermark and some other design features we have consistently used in past in our portfolio.  Included are two options for logos--vertical and horizontal.
**I also would like to remove "Member of Sight Alliance" on our logo if possible**
 Other image files available upon request.

Target Market(s)

New patient & Current Patients

Industry/Entity Type

Optometry

Contact Information for Business Card

High-tech optometry practice with 3 doctors seeking new business card.  We provide eye exams, sell, designer glasses/contacts/specialty eyewear and treat ocular diseases.  For our business cards, we are seeking fresh, clean, and crisp design as we grow our team (staffing change).  Simply adding doctors is making the card look busy/cluttered.  Looking for professional, less cluttered look yet still have our logo, doctor names, phone, address, and website....If possible!  :) Names: Marcia Trelford, O.D. Ned Pallister, O.D. Oona Ferrant, O.D. Phone: 555-014-2738 Website: www.BrightLensHub.example Address:  417 Garnet R. Holloway, Larkmoor, ZZ 00000 Ultimately we have the main business card with all doctor sames and that card has two versions  (front is always the same).  The back has two designs (1) displays next appointment time/date, (2) for "general use" (non-appointment.)    I have attached what we have used in the past.   We also need a design template for each team member in our practice with their name, title, and email.   Those should be designed with the "general use" back (see attached). **Open to entirely new design so don't feel obligated to keep current format.  Need new perspective!  Also including our watermark and some other design features we have consistently used in past in our portfolio.  Included are two options for logos--vertical and horizontal. **I also would like to remove "Member of Sight Alliance" on our logo if possible**  Other image files available upon request.

Font styles to use
Other font styles liked:
• We have used Montserrat / Yellowtail in the past

Colors

Designer to choose colors to be used in the design.

Requirements
Must have
• Clean & Fresh Design with Logo / Info provided in description. Horizontal orientation. **I have included the CMYK colors we currently have in our logo.
Should not have
• Cluttered

```html
<!DOCTYPE html>
<html lang="en">
<head>
<meta charset="utf-8">
<title>Clearview Optics – Business Cards</title>
<link rel="stylesheet" href="https://fonts.googleapis.com/css2?family=Arimo:wght@400;700&display=swap">
<style>
  :root {
    --stage: #d4d4d4;
    --card: #ffffff;
    --aqua: #9fd8e5;
    --ink: #3e3e3e;
    --ink-soft: #5a5a5a;
    --rule: #555555;
    --band-grey: #9a9a9a;
    --pattern: #f1f5f7;
  }
  * { box-sizing: border-box; margin: 0; padding: 0; }
  html, body { width: 857px; height: 1200px; overflow: hidden; }
  body {
    background: var(--stage);
    font-family: "Arimo", Arial, sans-serif;
    position: relative;
  }
  .card {
    position: absolute;
    left: 200px;
    width: 465px;
    height: 279px;
    background: var(--card);
    border-radius: 12px;
    overflow: hidden;
  }
  .card--front { top: 109px; }
  .card--appointment { top: 439px; }
  .card--general { top: 769px; }

  .brand {
    position: absolute;
    display: flex;
    align-items: center;
    gap: 12px;
    color: var(--ink);
    font-weight: 400;
    letter-spacing: 0.5px;
    white-space: nowrap;
  }
  .brand__dot {
    border-radius: 50%;
    background: var(--aqua);
    flex: none;
  }
  .card--front .brand { left: 24px; top: 38px; font-size: 28px; }
  .card--front .brand__dot { width: 50px; height: 50px; }
  .card--appointment .brand { left: 68px; top: 32px; font-size: 30px; }
  .card--appointment .brand__dot { width: 56px; height: 56px; }

  .doctors {
    position: absolute;
    left: 31px;
    top: 138px;
    list-style: none;
    color: var(--aqua);
    font-weight: 700;
    font-size: 15px;
    line-height: 16px;
  }
  .practice {
    position: absolute;
    left: 31px;
    top: 199px;
    color: var(--aqua);
    font-size: 13px;
  }
  .address {
    position: absolute;
    left: 30px;
    top: 216px;
    color: var(--ink);
    font-size: 10.5px;
  }
  .divider {
    position: absolute;
    left: 30px;
    top: 232px;
    width: 401px;
    height: 1px;
    background: var(--aqua);
  }
  .contact {
    position: absolute;
    top: 240px;
    display: flex;
    align-items: center;
    gap: 8px;
    color: var(--ink);
    font-size: 10.5px;
  }
  .contact--phone { left: 29px; }
  .contact--web { left: 150px; }
  .contact svg { width: 13px; height: 13px; }

  .band {
    position: absolute;
    left: 0;
    bottom: 0;
    width: 100%;
    height: 7px;
    background: var(--aqua);
  }
  .band--thin { height: 6px; }
  .band__accent {
    position: absolute;
    left: 0;
    bottom: 0;
    width: 48px;
    height: 7px;
    background: var(--band-grey);
    clip-path: polygon(0 0, 100% 0, 88% 100%, 0 100%);
  }

  .appointment__title {
    position: absolute;
    left: 0;
    width: 100%;
    top: 107px;
    text-align: center;
    color: var(--aqua);
    font-weight: 700;
    font-size: 17px;
    letter-spacing: 0.5px;
  }
  .slot {
    position: absolute;
    left: 32px;
    right: 30px;
    display: flex;
    align-items: flex-end;
    font-size: 10.5px;
    color: var(--ink-soft);
    letter-spacing: 0.5px;
  }
  .slot--first { top: 150px; }
  .slot--second { top: 190px; }
  .slot__line { height: 1px; background: var(--rule); margin: 0 8px 4px 10px; }
  .slot__line--date { flex: 1 1 auto; }
  .slot__line--time { width: 88px; margin-right: 0; }
  .notice {
    position: absolute;
    left: 0;
    width: 100%;
    top: 235px;
    text-align: center;
    font-size: 10.5px;
    line-height: 13px;
    color: var(--ink-soft);
    letter-spacing: 0.5px;
  }

  .watermark-field {
    position: absolute;
    inset: 0;
    background: var(--pattern);
  }
  .card--general .brand {
    right: 24px;
    bottom: 44px;
    font-size: 13px;
    gap: 8px;
  }
  .card--general .brand__dot { width: 34px; height: 34px; }
</style>
</head>
<body>

  <section class="card card--front" aria-label="Business card front">
    <div class="brand"><span class="brand__dot"></span><span class="brand__name">Clearview Optics</span></div>
    <ul class="doctors">
      <li>Marcia Trelford, O.D.</li>
      <li>Ned Pallister, O.D.</li>
      <li>Oona Ferrant, O.D.</li>
    </ul>
    <p class="practice">Clearview Optics</p>
    <p class="address">417 Garnet R. Holloway, Larkmoor, ZZ 00000</p>
    <div class="divider"></div>
    <p class="contact contact--phone">
      <svg viewBox="0 0 14 14" aria-hidden="true"><circle cx="7" cy="7" r="7" fill="var(--aqua)"/><path d="M4.5 5.5c0-1 1-1.5 2.5-1.5s2.5.5 2.5 1.5H8.4V5H5.6v.5zM4.8 6.3h4.4l.6 3.5H4.2z" fill="#fff"/></svg>
      555-014-2738
    </p>
    <p class="contact contact--web">
      <svg viewBox="0 0 14 14" aria-hidden="true"><circle cx="7" cy="7" r="7" fill="var(--aqua)"/><circle cx="7" cy="7" r="4" fill="none" stroke="#fff" stroke-width="1"/><path d="M3 7h8M7 3c-1.6 2.4-1.6 5.6 0 8M7 3c1.6 2.4 1.6 5.6 0 8" fill="none" stroke="#fff" stroke-width=".8"/></svg>
      www.BrightLensHub.example
    </p>
    <div class="band"></div>
    <div class="band__accent"></div>
  </section>

  <section class="card card--appointment" aria-label="Appointment card back">
    <div class="brand"><span class="brand__dot"></span><span class="brand__name">Clearview Optics</span></div>
    <h2 class="appointment__title">Your Next Appointetment</h2>
    <div class="slot slot--first">
      <span>Date</span><span class="slot__line slot__line--date"></span>
      <span>Time</span><span class="slot__line slot__line--time"></span>
    </div>
    <div class="slot slot--second">
      <span>Date</span><span class="slot__line slot__line--date"></span>
      <span>Time</span><span class="slot__line slot__line--time"></span>
    </div>
    <p class="notice">If your unable to keep your appoinment<br>kindly give us 24 hour notice</p>
    <div class="band band--thin"></div>
  </section>

  <section class="card card--general" aria-label="General use card back">
    <div class="watermark-field" role="img" aria-label="Faint repeating brand watermark pattern"></div>
    <div class="brand"><span class="brand__dot"></span><span class="brand__name">Clearview Optics</span></div>
  </section>

</body>
</html>
```